Please create a custom website design for Cedar Links Institute.

We need a 2 page design.

1. page
Home

Blue Logo
Headline: Home, instructors, Programs, Teaching Video
Club reviews, Event, Member's area, Contact & Location

Please combine 3 coaches golf swing (attached) to one big picture and use other background maybe a golf course or something

3-4 video thumbnails links(Photo attached)
title: About Cedar links,Instrutional video, Club reviews, Event etc.

Welcome to cedar links......
Members Voice

Footline:
Partners Varnholt, Swingpath, QEL rollbox...etc

2. page

Instructors (Photo attached )

Darren Okoye (Blue shirt) Photo + 1 video Thumbnail
Founder/ Director
WLFA Tour Pro/Teaching Pro (A)
ICMRB Lv 3 Certified Instrutor
Trained at Rolf Ebbing School of Golf
Trained at Japan Kawanobeyama Country club
Harbourline Institute of Technology

Tessa Marlow (white shirt) Photo + 1 video Thumbnail
Teaching Director/Head Coach
Teaching Director/Head coach
- Member of European KFLA
Member of Germany KFLA
Member of UK KFLA
ICMRB Lv3 Certified Instructor
Europe Emerging Circuit(1999-02)

Felix Ortan(black shirt) Photo + 1 video Thumbnail

WLFA Teaching Pro (A)
WLFA National Mentor Shield Champion2014
Brookvale Golf College Australia

The logo is attached to this brief.

Preferred colours could be based on Blue
Here is the link to the logo project: http://briefs.pixelvenue.example/task.aspx?id=413577

Target Market(s)

Golfers

Industry/Entity Type

Golf Course

Number of Pages Required

2 page

Font styles to use
Sans Serif

Colors
0555a3
ffffff
ec2027

Requirements
Must have
• The photos provided
• Blue based Webpage
Nice to have
• Other golf photos
• a little touch of red color

```html
<!DOCTYPE html>
<html lang="en">
<head>
<meta charset="utf-8">
<title>Cedar Links Institute</title>
<link rel="stylesheet" href="https://fonts.googleapis.com/css2?family=Oswald:wght@400;500;700&family=Open+Sans:wght@400;600;700&display=swap">
<style>
:root{
  --blue:#0555a3;
  --blue-dark:#043f7a;
  --red:#ec2027;
  --white:#ffffff;
  --ink:#3c3c3c;
  --muted:#777777;
  --night:#24272b;
  --night-2:#2f3338;
  --footer:#2a2d31;
  --grass:#5f8f3a;
}
*{box-sizing:border-box;margin:0;padding:0}
html,body{width:1200px;height:2660px;overflow:hidden}
body{position:relative;font-family:"Open Sans",Arial,sans-serif;color:var(--ink);background:var(--white)}
.abs{position:absolute}
h2,h3,.nav a,.hero-title,.hero-sub,.box-title{font-family:"Oswald",Arial Narrow,sans-serif}

/* hero */
.hero{left:0;top:0;width:1200px;height:540px;background:linear-gradient(180deg,#4d86bf 0%,#8dbbe0 30%,#7aa36a 62%,#4d7d2d 100%)}
.brand{left:0;top:52px;width:1200px;text-align:center;color:var(--white);font-family:"Open Sans",sans-serif;font-weight:700;font-size:34px;letter-spacing:.5px}
.nav{left:0;top:170px;width:1200px;height:30px;background:rgba(5,85,163,.88);display:flex;justify-content:center;gap:30px;align-items:center}
.nav a{color:var(--white);text-decoration:none;font-size:14px;text-transform:uppercase;letter-spacing:.5px}
.hero-title{left:0;top:392px;width:1200px;text-align:center;color:var(--white);font-size:44px;font-weight:700;text-transform:uppercase;text-shadow:0 2px 6px rgba(0,0,0,.4)}
.hero-sub{left:0;top:456px;width:1200px;text-align:center;color:var(--white);font-size:20px;letter-spacing:1px;text-transform:uppercase}

/* feature boxes */
.box{top:510px;width:220px;height:130px;color:var(--white);text-align:center}
.box.blue{background:var(--blue)}
.box.red{background:var(--red)}
.box-icon{position:absolute;left:80px;top:-30px;width:60px;height:60px;border-radius:50%;background:inherit;border:4px solid var(--white);display:flex;align-items:center;justify-content:center}
.box-title{position:absolute;left:0;top:44px;width:100%;font-size:18px;line-height:22px;text-transform:uppercase}
.box-go{position:absolute;left:100px;top:102px;width:20px;height:20px;border-radius:50%;background:var(--white);display:flex;align-items:center;justify-content:center}

/* welcome */
.section-title{color:var(--blue);font-size:28px;font-weight:500;text-transform:uppercase;text-align:center}
.rule{height:2px;width:80px;background:var(--red);margin:10px auto 0}
.welcome{left:200px;top:660px;width:800px}
.welcome p{margin-top:24px;font-size:14px;line-height:24px;color:var(--muted);text-align:center}
.btn{display:block;width:110px;margin:26px auto 0;padding:8px 0;background:var(--blue);color:var(--white);font-size:12px;font-weight:700;text-align:center;text-transform:uppercase;text-decoration:none}

/* dark band 1 */
.band{left:0;width:1200px;background:linear-gradient(180deg,var(--night) 0%,var(--night-2) 100%)}
.band .section-title{color:var(--white)}
.video-frame{left:224px;top:1132px;width:310px;height:288px;background:linear-gradient(180deg,#8eaac4 0%,#6f9456 55%,#3f6a27 100%)}
.play-big{left:354px;top:1251px;width:50px;height:50px;border-radius:50%;border:3px solid var(--white);display:flex;align-items:center;justify-content:center}
.review{left:628px;width:360px;display:flex;gap:16px}
.play{flex:none;width:56px;height:56px;border-radius:50%;border:3px solid #cfd4da;display:flex;align-items:center;justify-content:center}
.review p{font-size:13px;line-height:19px;color:#d6d9dd}
.review a{color:var(--white);font-size:12px;text-decoration:none}

/* events */
.events{left:0;top:1460px;width:1200px;height:380px;background:var(--white)}
.event{top:1672px;width:360px;display:flex;gap:14px}
.thumb{flex:none;width:50px;height:50px;border-radius:50%;background:radial-gradient(circle,#7fae54,#3f6d22)}
.event h4{font-size:14px;line-height:19px;color:var(--blue);font-weight:700}
.event p{font-size:12px;line-height:18px;color:var(--muted);margin-top:4px}
.event .date{font-size:11px;color:#9a9a9a;margin-top:4px}
.arrow{top:1700px;width:30px;height:40px;display:flex;align-items:center;justify-content:center}

/* instructors band */
.card{top:2020px;width:150px;height:290px;background:var(--white)}
.card .photo{width:150px;height:252px;background:linear-gradient(180deg,#dfe7ee 0%,#b7c7d6 100%)}
.card .label{height:38px;color:var(--white);font-family:"Oswald",sans-serif;font-size:14px;text-transform:uppercase;display:flex;align-items:center;justify-content:center}
.voice{left:640px;width:340px;display:flex;gap:14px}
.avatar{flex:none;width:52px;height:52px;border-radius:50%;background:#8d949c;border:2px solid #c9ced4}
.voice p{font-size:12px;line-height:18px;color:#d6d9dd}
.voice .who{color:var(--white);font-size:12px;margin-top:4px}

/* footer */
.footer{left:0;top:2340px;width:1200px;height:320px;background:var(--footer);text-align:center}
.footer .brand-foot{position:absolute;left:0;top:76px;width:100%;color:#c8ccd1;font-weight:700;font-size:26px}
.footer .links{position:absolute;left:0;top:172px;width:100%;font-size:12px;color:#aeb3b9;display:flex;justify-content:center;gap:22px}
.footer .copy{position:absolute;left:0;top:200px;width:100%;font-size:11px;color:#8b9197}
.social{position:absolute;left:540px;top:250px;display:flex;gap:12px}
.social span{width:28px;height:28px;border-radius:50%;border:2px solid #aeb3b9}
</style>
</head>
<body>

<header class="abs hero" role="img" aria-label="Golfer mid-swing on a sunlit course framed by trees"></header>
<div class="abs brand">Cedar Links Institute</div>
<nav class="abs nav">
  <a href="#">Home</a><a href="#">Instructors</a><a href="#">Programs</a><a href="#">Teaching Video</a>
  <a href="#">Club Reviews</a><a href="#">Event</a><a href="#">Member's Area</a><a href="#">Contact &amp; Location</a>
</nav>
<div class="abs hero-title">World's Best Golf Academy</div>
<div class="abs hero-sub">Setting the standard for golf school instruction since 1971</div>

<section class="abs box blue" style="left:228px">
  <div class="box-icon"><svg width="22" height="28" viewBox="0 0 22 28"><path d="M11 1a10 10 0 0 0-10 10c0 7 10 16 10 16s10-9 10-16A10 10 0 0 0 11 1z" fill="#fff"/><circle cx="11" cy="11" r="4" fill="#0555a3"/></svg></div>
  <div class="box-title">Find the perfect<br>location</div>
  <div class="box-go"><svg width="8" height="10" viewBox="0 0 8 10"><path d="M1 1l5 4-5 4" stroke="#0555a3" stroke-width="2" fill="none"/></svg></div>
</section>
<section class="abs box red" style="left:490px">
  <div class="box-icon"><svg width="30" height="20" viewBox="0 0 30 20"><rect x="1" y="2" width="19" height="16" rx="2" fill="#fff"/><path d="M21 8l8-5v14l-8-5z" fill="#fff"/></svg></div>
  <div class="box-title">See our teaching<br>videos</div>
  <div class="box-go"><svg width="8" height="10" viewBox="0 0 8 10"><path d="M1 1l5 4-5 4" stroke="#ec2027" stroke-width="2" fill="none"/></svg></div>
</section>
<section class="abs box blue" style="left:752px">
  <div class="box-icon"><svg width="24" height="24" viewBox="0 0 24 24"><path d="M12 2v20M2 12h20" stroke="#fff" stroke-width="4"/></svg></div>
  <div class="box-title">Want to become<br>a member</div>
  <div class="box-go"><svg width="8" height="10" viewBox="0 0 8 10"><path d="M1 1l5 4-5 4" stroke="#0555a3" stroke-width="2" fill="none"/></svg></div>
</section>

<section class="abs welcome">
  <h2 class="section-title">Welcome to Cedar Links Institute</h2>
  <div class="rule"></div>
  <p>Whether you are taking up the game or chasing a lower handicap, our coaches help golfers of every level reach new heights. Our academy has shaped players for decades through patient teaching, modern swing analysis and honest feedback. Students train on full practice grounds, short game areas and covered bays in every season. Lessons are built around your goals, your body and your schedule, so progress feels natural. Join us for a first session and see how far your game can go with the right guidance.</p>
  <a class="btn" href="#">Learn more</a>
</section>

<section class="abs band" style="top:1000px;height:460px"></section>
<h2 class="abs section-title" style="left:224px;top:1036px;width:310px;color:#fff">Instructional Video</h2>
<h2 class="abs section-title" style="left:628px;top:1036px;width:360px;color:#fff">Club Reviews</h2>
<div class="abs video-frame" role="img" aria-label="Coach demonstrating a full swing on the practice range"></div>
<div class="abs play-big"><svg width="16" height="18" viewBox="0 0 16 18"><path d="M2 1l13 8-13 8z" fill="#fff"/></svg></div>

<article class="abs review" style="top:1132px">
  <div class="play"><svg width="16" height="18" viewBox="0 0 16 18"><path d="M2 1l13 8-13 8z" fill="#fff"/></svg></div>
  <div><p>Our fitting team tests the latest drivers and irons so you can choose clubs that suit your swing speed.</p><a href="#">read more</a></div>
</article>
<article class="abs review" style="top:1244px">
  <div class="play"><svg width="16" height="18" viewBox="0 0 16 18"><path d="M2 1l13 8-13 8z" fill="#fff"/></svg></div>
  <div><p>A close look at new putters this season, with notes on feel, balance and alignment for every stroke.</p><a href="#">read more</a></div>
</article>
<article class="abs review" style="top:1352px">
  <div class="play"><svg width="16" height="18" viewBox="0 0 16 18"><path d="M2 1l13 8-13 8z" fill="#fff"/></svg></div>
  <div><p>Wedges compared side by side on spin, turf contact and control from tight lies around the green.</p><a href="#">read more</a></div>
</article>

<section class="abs events"></section>
<h2 class="abs section-title" style="left:0;top:1548px;width:1200px">Latest Events</h2>
<div class="abs rule" style="left:560px;top:1596px"></div>
<div class="abs arrow" style="left:170px"><svg width="14" height="26" viewBox="0 0 14 26"><path d="M12 2L2 13l10 11" stroke="#bbb" stroke-width="2" fill="none"/></svg></div>
<article class="abs event" style="left:240px">
  <div class="thumb" role="img" aria-label="Golf course event thumbnail"></div>
  <div><h4>Spring junior clinic opens for new players this April.</h4><p>Four weekend sessions covering grip, stance and course manners for young golfers. <span style="color:#0555a3">read more</span></p><div class="date">Posted on 08.11.2024</div></div>
</article>
<article class="abs event" style="left:632px">
  <div class="thumb" role="img" aria-label="Golf course event thumbnail"></div>
  <div><h4>Members' autumn cup returns with a shotgun start.</h4><p>Eighteen holes, team scoring and a relaxed dinner at the clubhouse afterward. <span style="color:#0555a3">read more</span></p><div class="date">Posted on 08.11.2024</div></div>
</article>
<div class="abs arrow" style="left:1000px"><svg width="14" height="26" viewBox="0 0 14 26"><path d="M2 2l10 11L2 24" stroke="#bbb" stroke-width="2" fill="none"/></svg></div>

<section class="abs band" style="top:1840px;height:500px;background:linear-gradient(180deg,#3b4a3a 0%,#2d3a2c 100%)" role="img" aria-label="Blurred golf course backdrop"></section>
<h2 class="abs section-title" style="left:220px;top:1916px;width:320px;color:#fff">Our Instructors</h2>
<h2 class="abs section-title" style="left:640px;top:1916px;width:340px;color:#fff">Member Voice</h2>
<div class="abs arrow" style="left:180px;top:2140px"><svg width="14" height="26" viewBox="0 0 14 26"><path d="M12 2L2 13l10 11" stroke="#fff" stroke-width="2" fill="none"/></svg></div>
<article class="abs card" style="left:224px">
  <div class="photo" role="img" aria-label="Portrait of instructor Tessa Marlow"></div>
  <div class="label" style="background:var(--blue)">Tessa Marlow</div>
</article>
<article class="abs card" style="left:380px">
  <div class="photo" role="img" aria-label="Portrait of instructor Darren Okoye"></div>
  <div class="label" style="background:var(--red)">Darren Okoye</div>
</article>
<div class="abs arrow" style="left:548px;top:2140px"><svg width="14" height="26" viewBox="0 0 14 26"><path d="M2 2l10 11L2 24" stroke="#fff" stroke-width="2" fill="none"/></svg></div>

<article class="abs voice" style="top:1990px">
  <div class="avatar" role="img" aria-label="Member portrait"></div>
  <div><p>The coaches fixed my slice in three lessons and explained every change clearly along the way.</p><div class="who">Mr. Owen Palliser</div></div>
</article>
<article class="abs voice" style="top:2092px">
  <div class="avatar" role="img" aria-label="Member portrait"></div>
  <div><p>Friendly staff, great practice facilities and video reviews that really show what to work on.</p><div class="who">Mr. Rhys Tamburlane</div></div>
</article>
<article class="abs voice" style="top:2198px">
  <div class="avatar" role="img" aria-label="Member portrait"></div>
  <div><p>I dropped six shots this season thanks to a short game plan built just for me.</p><div class="who">Mr. L. Verhoek</div></div>
</article>

<footer class="abs footer">
  <div class="brand-foot">Cedar Links Institute</div>
  <div class="links"><span>Home</span><span>Instructors</span><span>Programs</span><span>Teaching Video</span><span>Club Reviews</span><span>Event</span><span>Member's Area</span><span>Contact &amp; Location</span></div>
  <div class="copy">© 2024 Cedar Links Institute. All rights reserved. Privacy Policy | Terms of Use</div>
  <div class="social"><span></span><span></span><span></span><span></span></div>
</footer>

</body>
</html>
```